Flyer für unser Jubiläumscamp "herbstcamp"

Am 10. - 14.10.2022 und 17. - 21. 10.2022 organisieren wir je eine Woche ein Fussballcamp für Kinder ab 5 Jahren bis 12 Jahren. Ebenfalls feiern wir unser 5 jähriges Jubiläum und bieten deshalb das Camp für 300 statt 350 CHF an.
Für dieses Camp (mit dieses 2 Angeboten) möchten wir einen speziellen Flyer haben. Der Flyedr sollte Kinder freundlich aber auch modern sein. Wir bieten auch ein Leistungs, Girls Only sowie ein Goalicamp. (eventuell ist dies aber zu überlastet dan)
Infos zu unseren Camps: https://balltaler.ch/events/2022-sommercamps-juli/

Kinder, 5-12 Jahre

• Logo, Fun Kidscamp
• Gleiches wie der Flyer angehängt.

```html
<!DOCTYPE html>
<html lang="de">
<head>
<meta charset="utf-8">
<title>Soccer Camp – Balltaler</title>
<link rel="stylesheet" href="https://fonts.googleapis.com/css2?family=Poppins:wght@500;600;700&family=Oswald:wght@600&family=Graduate&display=swap">
<style>
  :root {
    --navy: #253f7a;
    --navy-dark: #1d3266;
    --orange: #f36f12;
    --orange-light: #f7931e;
    --grass: #3d9a2c;
    --grass-dark: #2c7a1f;
    --paper: #f3f3f3;
    --ink: #1a1a1a;
    --stage: #e9e9ea;
    --photo-a: #3557a8;
    --photo-b: #1f3b82;
  }
  * { margin: 0; padding: 0; box-sizing: border-box; }
  html, body { width: 1200px; height: 2398px; overflow: hidden; background: var(--stage); }
  body { position: relative; font-family: "Poppins", sans-serif; }

  .flyer {
    position: absolute; left: 69px; top: 512px;
    width: 1062px; height: 1374px; overflow: hidden;
    background: var(--paper);
    box-shadow: 0 8px 22px rgba(0,0,0,.28);
  }
  .flyer-backdrop { position: absolute; inset: 0; }

  .photo {
    position: absolute; border-radius: 40px;
    background: radial-gradient(ellipse at center, var(--photo-a) 0%, var(--photo-b) 70%, transparent 100%);
    opacity: .85;
  }
  .photo--left { left: 0; top: 10px; width: 400px; height: 430px; }
  .photo--right { left: 790px; top: 15px; width: 272px; height: 505px; }
  .photo--player { left: 765px; top: 775px; width: 297px; height: 575px;
    background: radial-gradient(ellipse at center, #2b4fa3 0%, #c9cfda 75%, transparent 100%); }

  .headline { position: absolute; left: 300px; top: 50px; width: 480px; height: 300px; }

  .age-pill {
    position: absolute; left: 366px; top: 362px; width: 330px; height: 46px;
    background: #fff; border-radius: 8px;
    color: var(--navy); font-weight: 700; font-size: 31px;
    display: flex; align-items: center; justify-content: center; letter-spacing: .5px;
  }

  .club-badge {
    position: absolute; left: 70px; top: 440px; width: 300px; height: 300px;
    border-radius: 50%; background: #fff; border: 9px solid var(--orange);
    display: flex; align-items: center; justify-content: center;
  }
  .club-badge__name { font-weight: 700; font-size: 48px; color: var(--navy); }

  .jubilee-number {
    position: absolute; left: 470px; top: 628px;
    font-family: "Oswald", sans-serif; font-weight: 600; font-size: 130px; line-height: 1;
    color: var(--orange);
  }
  .jubilee-text { position: absolute; left: 545px; top: 652px; color: var(--navy); line-height: 1.2; }
  .jubilee-text__top { font-size: 37px; font-weight: 500; }
  .jubilee-text__bottom { font-size: 42px; font-weight: 700; }
  .bursts { position: absolute; left: 410px; top: 590px; width: 640px; height: 220px; }

  .month {
    position: absolute; left: 63px; top: 818px;
    font-size: 64px; font-weight: 600; color: var(--navy); line-height: 1;
  }
  .dates {
    position: absolute; left: 133px; top: 905px;
    font-size: 38px; font-weight: 700; color: var(--ink); white-space: nowrap;
  }
  .dates sup { font-size: 20px; vertical-align: 16px; margin-right: 10px; }
  .dates .amp { color: var(--navy); margin: 0 14px 0 6px; }
  .camp-type {
    position: absolute; left: 62px; top: 1000px;
    font-size: 38px; font-weight: 600; color: var(--ink); white-space: nowrap;
  }
  .rules { position: absolute; left: 0; top: 0; width: 1062px; height: 1374px; pointer-events: none; }

  .info-tab {
    position: absolute; left: 0; top: 1137px; width: 433px; height: 58px;
    background: var(--navy); border-radius: 0 12px 12px 0;
    color: #fff; font-size: 22px; font-weight: 600;
    display: flex; align-items: center; padding-left: 62px;
  }
  .contact { position: absolute; left: 63px; font-size: 25px; font-weight: 500; color: var(--ink);
    display: flex; align-items: center; gap: 22px; white-space: nowrap; }
  .contact--web { top: 1218px; }
  .contact--mail { top: 1262px; }
  .contact svg { width: 22px; height: 22px; flex: none; }
</style>
</head>
<body>
<main class="flyer">
  <svg class="flyer-backdrop" viewBox="0 0 1062 1374" aria-hidden="true">
    <defs>
      <linearGradient id="field" x1="0" y1="0" x2="0" y2="1">
        <stop offset="0" stop-color="#f7f7f7"/>
        <stop offset="1" stop-color="#ececec"/>
      </linearGradient>
    </defs>
    <rect width="1062" height="1374" fill="url(#field)"/>
    <path d="M0 0H1062V590C900 520 700 480 370 570 240 560 100 560 0 575Z" fill="var(--navy)"/>
    <path d="M370 570C600 505 820 500 1062 590V635C820 560 600 550 370 595Z" fill="var(--grass)"/>
    <path d="M370 595C600 550 820 560 1062 635" fill="none" stroke="var(--orange)" stroke-width="5"/>
    <path d="M0 575C100 560 240 560 370 570" fill="none" stroke="var(--orange)" stroke-width="5"/>
    <rect x="0" y="1323" width="1062" height="6" fill="var(--orange-light)"/>
    <rect x="0" y="1329" width="1062" height="45" fill="var(--grass)"/>
    <rect x="0" y="1355" width="1062" height="19" fill="var(--grass-dark)"/>
  </svg>

  <div class="photo photo--left" role="img" aria-label="Zwei Kinder in blauen Trikots beim Fussballspielen mit Ball"></div>
  <div class="photo photo--right" role="img" aria-label="Zwei Kinder in blauen Trikots beim Zweikampf um einen Fussball"></div>

  <svg class="headline" viewBox="0 0 480 300" role="img" aria-label="Soccer Camp">
    <defs>
      <linearGradient id="titleFill" x1="0" y1="0" x2="0" y2="1">
        <stop offset="0.5" stop-color="#ffffff"/>
        <stop offset="0.5" stop-color="#9b9b9b"/>
      </linearGradient>
    </defs>
    <g font-family="Graduate, serif" text-anchor="middle" fill="url(#titleFill)"
       stroke="var(--navy-dark)" stroke-width="4" paint-order="stroke">
      <text x="240" y="130" font-size="118" textLength="420" lengthAdjust="spacingAndGlyphs" transform="scale(1 1.05)">SOCCER</text>
      <text x="240" y="265" font-size="118" textLength="315" lengthAdjust="spacingAndGlyphs" transform="translate(0 -8) scale(1 1.05)">CAMP</text>
    </g>
  </svg>

  <div class="age-pill">VON 5–14 JAHREN</div>

  <div class="club-badge"><span class="club-badge__name">Balltaler</span></div>

  <svg class="bursts" viewBox="0 0 640 220" aria-hidden="true" stroke="var(--orange)" stroke-width="6" stroke-linecap="round">
    <line x1="20" y1="50" x2="50" y2="80"/><line x1="65" y1="10" x2="70" y2="42"/>
    <line x1="8" y1="95" x2="40" y2="97"/><line x1="25" y1="190" x2="50" y2="172"/>
    <line x1="80" y1="210" x2="75" y2="182"/><line x1="625" y1="40" x2="595" y2="75"/>
    <line x1="545" y1="40" x2="550" y2="62"/><line x1="630" y1="110" x2="600" y2="122"/>
  </svg>
  <div class="jubilee-number">5</div>
  <div class="jubilee-text">
    <div class="jubilee-text__top">WIR FEIERN UNSER</div>
    <div class="jubilee-text__bottom">JÄHRIGES JUBILÄUM</div>
  </div>

  <div class="photo photo--player" role="img" aria-label="Junge im blauen Trikot jongliert einen Fussball"></div>

  <div class="month">OKTOBER</div>
  <div class="dates">10<sup>TH</sup>– 14<sup>TH</sup><span class="amp">&amp;</span>17<sup>TH</sup>– 21<sup>TH</sup></div>
  <div class="camp-type">EINWÖCHIGES FUßBALLCAMP</div>

  <svg class="rules" viewBox="0 0 1062 1374" aria-hidden="true">
    <line x1="395" y1="858" x2="600" y2="858" stroke="var(--orange)" stroke-width="4"/>
    <line x1="63" y1="983" x2="663" y2="983" stroke="var(--navy)" stroke-width="4"/>
    <path d="M679 920V1080Q679 1089 670 1089H110" fill="none" stroke="var(--orange)" stroke-width="4"/>
    <rect x="66" y="1082" width="52" height="14" rx="4" fill="var(--orange)"/>
    <g transform="translate(665 860)">
      <polygon fill="var(--orange-light)" points="0,-74 16,-62 35,-66 44,-48 63,-42 62,-22 75,-6 64,11 68,31 50,41 44,60 24,60 8,75 -8,62 -28,68 -38,50 -58,44 -60,24 -74,10 -64,-8 -68,-28 -50,-38 -42,-58 -22,-60 -8,-74"/>
      <g font-family="Oswald, sans-serif" font-weight="600" text-anchor="middle" transform="rotate(-8)">
        <text y="-24" font-size="20" fill="var(--ink)">350 CHF</text>
        <line x1="-32" y1="-30" x2="32" y2="-30" stroke="var(--ink)" stroke-width="2"/>
        <text y="18" font-size="36" fill="#fff">300 CHF</text>
      </g>
    </g>
  </svg>

  <div class="info-tab">FÜR MEHR INFORMATIONEN</div>
  <div class="contact contact--web">
    <svg viewBox="0 0 24 24" aria-hidden="true" fill="none" stroke="var(--orange)" stroke-width="2.2">
      <circle cx="12" cy="12" r="10"/><ellipse cx="12" cy="12" rx="4.5" ry="10"/>
      <line x1="2" y1="12" x2="22" y2="12"/><line x1="4" y1="7" x2="20" y2="7"/><line x1="4" y1="17" x2="20" y2="17"/>
    </svg>
    <span>https://balltaler.ch/events/2022-sommercamps-juli/</span>
  </div>
  <div class="contact contact--mail">
    <svg viewBox="0 0 24 24" aria-hidden="true">
      <rect x="1" y="5" width="22" height="15" rx="1.5" fill="var(--orange)"/>
      <path d="M2 6L12 14L22 6" fill="none" stroke="#fff" stroke-width="2"/>
    </svg>
    <span>info@balltaler.ch</span>
  </div>
</main>
</body>
</html>
```